Personal Training Company
Summit Vigor & Wellness
Project: Personal Training Company
Personal Training Company - Health
Creative Brief
Professional
Marla Brennick, MS, CSCS, CISSN
Charlotte, NC
summitvandwell@mailvista.com
taruk27 taruk27

```html
<!DOCTYPE html>
<html lang="en">
<head>
<meta charset="utf-8">
<title>Summit Vigor &amp; Wellness — Stationery Concepts</title>
<link href="https://fonts.googleapis.com/css2?family=Open+Sans:wght@400;700&family=Great+Vibes&display=swap" rel="stylesheet">
<style>
:root{
  --bg:#3b3b3b;
  --green:#8dc63f;
  --green-light:#c4e05a;
  --green-dark:#5f9a2a;
  --grey:#5a5a5a;
  --grey-dark:#2e2e2e;
  --paper:#ffffff;
  --paper-shade:#eeeeee;
  --ink:#4a4a4a;
  --muted:#9a9a9a;
}
*{box-sizing:border-box;margin:0;padding:0}
html,body{width:1200px;height:254px;overflow:hidden;background:var(--bg);font-family:"Open Sans",Arial,sans-serif;color:var(--ink)}
.sheet{position:relative;width:1200px;height:254px}
.piece{position:absolute;overflow:hidden}
.caption{position:absolute;font-size:2.6px;color:#cfcfcf;text-align:center;width:100%;bottom:-5px}
.holder{position:absolute}

.brand{display:flex;align-items:center;gap:2px;font-weight:700;white-space:nowrap;line-height:1}
.brand .dot{border-radius:50%;flex:none}
.brand.on-green,.brand.on-dark{color:var(--paper)}
.brand.on-green .dot,.brand.on-dark .dot{background:var(--paper)}
.brand.on-light{color:var(--grey)}
.brand.on-light .dot{background:var(--green)}

.intro{left:30px;top:30px;width:70px;text-align:center;color:var(--paper)}
.intro .brand{font-size:5.6px;justify-content:center}
.intro .brand .dot{width:7px;height:7px}
.intro p{font-size:3.6px;margin-top:4px;color:#ddd}

.card{width:48px;height:25px;border-radius:1px;padding:4px}
.card .brand{font-size:4px}
.card .brand .dot{width:5px;height:5px}
.card small{display:block;font-size:1.8px;margin-top:3px}
.card.green{background:linear-gradient(135deg,var(--green-light),var(--green))}
.card.grey{background:linear-gradient(135deg,#6a6a6a,var(--grey-dark));color:#eee}
.card.white{background:var(--paper)}

.page{background:var(--paper);padding:5px}
.page .brand{font-size:3.6px}
.page .brand .dot{width:4px;height:4px}
.page .lines p{font-size:1.7px;line-height:2.3px;color:#777;margin-top:2px}
.page .footer{position:absolute;left:0;right:0;bottom:0;height:3px;background:var(--grey)}
.page .footer::before{content:"";position:absolute;left:0;top:0;height:1px;width:100%;background:var(--green)}
.sig{font-family:"Great Vibes",cursive;font-size:6px;color:var(--grey);margin-top:3px}
.faint{position:absolute;border-radius:50%;background:var(--paper-shade)}

.envelope{background:var(--paper);padding:4px}
.envelope .brand{font-size:3.2px}
.envelope .brand .dot{width:4px;height:4px}
.flap-green{background:linear-gradient(180deg,var(--green-light),var(--green))}
.flap-grey{background:linear-gradient(180deg,#777,var(--grey))}

.folder{display:flex}
.folder .half{flex:1;position:relative}
.folder .left{background:radial-gradient(circle at 50% 45%,var(--green-light),var(--green) 70%)}
.folder .right{background:var(--paper);display:flex;align-items:center;justify-content:center}
.folder .right .brand{font-size:5px}
.folder .right .brand .dot{width:6px;height:6px}

.fax table{width:100%;border-collapse:collapse;margin-top:6px}
.fax td{font-size:1.6px;border-bottom:0.3px solid #ccc;height:3.2px;color:#888}
.fax td.box{background:var(--paper-shade)}

.slip .script,.thanks .script{font-family:"Great Vibes",cursive;color:var(--green);font-size:7px;margin-top:4px}

.disc{border-radius:50%;display:flex;align-items:center;justify-content:center;position:absolute}
.disc .hole{width:30%;height:30%;border-radius:50%;background:var(--bg);border:2px solid var(--paper)}
.disc .brand{position:absolute;top:18%;font-size:3.6px}
.disc .brand .dot{width:4px;height:4px}
.disc.green{background:radial-gradient(circle,var(--green-light),var(--green) 70%)}
.disc.grey{background:radial-gradient(circle,#777,#444 70%);border:1.5px solid var(--green)}
.disc.white{background:var(--paper);border:2px solid var(--green)}

.screen{display:flex;align-items:center;justify-content:center}
.screen.green{background:radial-gradient(circle,var(--green-light),var(--green) 75%)}
.screen.light{background:var(--paper)}
.screen.black{background:#111}
.screen .brand{font-size:4.2px}
.screen .brand .dot{width:5px;height:5px}

.slide{background:var(--paper);padding:4px 5px}
.slide h3{font-size:3.6px;color:var(--green);font-weight:700}
.slide h4{font-size:2px;color:var(--muted);font-weight:400;border-bottom:0.3px solid #ccc;padding-bottom:1px}
.slide p{font-size:1.6px;line-height:2.1px;color:#888;margin-top:1.5px}
.slide .bar{position:absolute;left:0;right:0;bottom:0;height:3px;background:var(--grey)}
.slide .corner{position:absolute;right:4px;top:4px;width:4px;height:4px;border-radius:50%;background:var(--green)}
.slide.title{text-align:center}
.slide.title .brand{font-size:6px;justify-content:center;margin-top:10px}
.slide.title .brand .dot{width:7px;height:7px}
.slide.title .welcome{font-size:3.6px;color:var(--green-dark);margin-top:8px}
.slide.title .name{font-size:5px;color:var(--green);font-weight:700}
.slide.title .desc{font-size:3.2px;color:#555}
.photos{display:flex;gap:3px;margin-top:3px}
.photos div{flex:1;height:14px;background:#555;color:#ccc;font-size:1.8px;display:flex;align-items:center;justify-content:center}
.slide.closing{background:radial-gradient(circle at 50% 50%,var(--green-light),var(--green) 75%);color:var(--paper);text-align:center;padding-top:20px}
.slide.closing .big{font-size:12px;font-weight:400;line-height:1}
.slide.closing .small{font-size:6px;line-height:1.1}
.magnet{position:absolute;width:20px;height:20px;border-radius:50%;display:flex;align-items:center;justify-content:center;border:1px solid #ccc}
.magnet .brand{font-size:2.4px}
.magnet .brand .dot{width:3px;height:3px}
</style>
</head>
<body>
<main class="sheet">

  <section class="holder intro">
    <div class="brand on-dark"><span class="dot"></span>Summit Vigor &amp; Wellness</div>
    <p>Stationery Concepts</p>
  </section>

  <!-- business cards -->
  <div class="piece card green" style="left:6px;top:58px"><div class="brand on-green"><span class="dot"></span>Summit Vigor</div><small style="color:#fff">www.summitvigorwell.com</small></div>
  <div class="piece card grey" style="left:58px;top:58px"><div class="brand on-dark"><span class="dot"></span>Summit Vigor</div><small>Marla Brennick<br>MS, CSCS, CISSN<br>(704) 555-0148</small></div>
  <div class="piece card white" style="left:6px;top:92px"><div class="brand on-light"><span class="dot"></span>Summit Vigor</div><small style="color:#888">www.summitvigorwell.com</small></div>
  <div class="piece card grey" style="left:58px;top:92px"><div class="brand on-dark"><span class="dot"></span>Summit Vigor</div><small>summitvandwell@mailvista.com</small></div>

  <!-- letterheads -->
  <article class="piece page" style="left:108px;top:15px;width:78px;height:102px">
    <div class="faint" style="left:34px;top:30px;width:44px;height:44px"></div>
    <div class="brand on-light" style="position:relative"><span class="dot"></span>Summit Vigor &amp; Wellness</div>
    <div class="lines" style="position:relative">
      <p>Date<br>Recipient Name<br>Company Name<br>Street Address<br>Charlotte, NC</p>
      <p>Thank you for choosing our personal training studio. We build each program around your goals, your schedule and your current level of fitness.</p>
      <p>Every session is planned with care, tracked over time and adjusted as you grow stronger, so steady progress becomes part of your week.</p>
      <p>We look forward to working with you.</p>
    </div>
    <div class="sig" style="position:relative">Signature</div>
    <div class="lines" style="position:relative"><p>Marla Brennick</p></div>
    <div class="footer"></div>
  </article>
  <article class="piece page" style="left:192px;top:15px;width:78px;height:102px">
    <div class="faint" style="left:34px;top:30px;width:44px;height:44px"></div>
    <div class="brand on-light" style="position:relative"><span class="dot"></span>Summit Vigor &amp; Wellness</div>
    <div class="lines" style="position:relative">
      <p>Date<br>Recipient Name<br>Company Name<br>Street Address<br>Charlotte, NC</p>
      <p>Thank you for choosing our personal training studio. We build each program around your goals, your schedule and your current level of fitness.</p>
      <p>Every session is planned with care, tracked over time and adjusted as you grow stronger.</p>
    </div>
    <div class="sig" style="position:relative">Signature</div>
    <div class="lines" style="position:relative"><p>Marla Brennick</p></div>
    <div class="footer"></div>
  </article>

  <!-- envelopes -->
  <div class="piece envelope" style="left:276px;top:80px;width:78px;height:36px"><div class="brand on-light"><span class="dot"></span>Summit Vigor &amp; Wellness</div></div>
  <div class="piece flap-green" style="left:372px;top:40px;width:78px;height:14px"></div>
  <div class="piece flap-grey" style="left:370px;top:58px;width:82px;height:14px"></div>
  <div class="piece envelope" style="left:364px;top:78px;width:88px;height:38px;text-align:center"><span style="font-size:2px;color:#888;display:block;margin-top:18px">www.summitvigorwell.com</span></div>

  <!-- folder -->
  <div class="piece folder" style="left:466px;top:18px;width:116px;height:98px">
    <div class="half left" role="img" aria-label="Soft green glow behind the brand symbol"></div>
    <div class="half right"><div class="brand on-light"><span class="dot"></span>Summit Vigor</div></div>
  </div>

  <!-- fax sheets -->
  <article class="piece page fax" style="left:594px;top:15px;width:78px;height:100px">
    <div class="brand on-light"><span class="dot"></span>Summit Vigor</div>
    <table><tr><td>To</td><td class="box"></td><td>From</td><td class="box"></td></tr><tr><td>Fax</td><td class="box"></td><td>Pages</td><td class="box"></td></tr><tr><td>Phone</td><td class="box"></td><td>Date</td><td class="box"></td></tr><tr><td>Re</td><td class="box"></td><td>CC</td><td class="box"></td></tr></table>
    <div class="lines"><p>Comments:</p></div>
    <div class="footer"></div>
  </article>
  <article class="piece page fax" style="left:678px;top:15px;width:78px;height:100px">
    <div class="brand on-light"><span class="dot"></span>Summit Vigor</div>
    <table><tr><td>To</td><td class="box"></td><td>From</td><td class="box"></td></tr><tr><td>Fax</td><td class="box"></td><td>Pages</td><td class="box"></td></tr><tr><td>Phone</td><td class="box"></td><td>Date</td><td class="box"></td></tr><tr><td>Re</td><td class="box"></td><td>CC</td><td class="box"></td></tr></table>
    <div class="lines"><p>Comments:</p></div>
    <div class="footer"></div>
  </article>

  <!-- compliments slip & thank you cards -->
  <div class="piece page slip" style="left:770px;top:27px;width:84px;height:36px"><div class="brand on-light"><span class="dot"></span>Summit Vigor</div><div class="script">With Compliments</div><div class="footer"></div></div>
  <div class="piece page thanks" style="left:764px;top:72px;width:50px;height:38px"><div class="brand on-light"><span class="dot"></span>Summit Vigor</div><div class="script">Thank you</div></div>
  <div class="piece screen green" style="left:818px;top:72px;width:50px;height:38px"></div>

  <!-- CD and cover -->
  <div class="disc green" style="left:870px;top:6px;width:58px;height:58px"><div class="brand on-green"><span class="dot"></span>Summit Vigor</div><div class="hole"></div></div>
  <div class="piece page" style="left:934px;top:10px;width:56px;height:50px"><div class="brand on-light"><span class="dot"></span>Summit Vigor</div><div class="footer" style="height:2px"></div></div>

  <!-- screens -->
  <div class="piece screen green" style="left:872px;top:72px;width:56px;height:40px"><div class="brand on-green"><span class="dot"></span>Summit Vigor</div></div>
  <div class="piece screen green" style="left:940px;top:74px;width:16px;height:34px"></div>
  <div class="piece screen black" style="left:966px;top:74px;width:16px;height:34px"></div>

  <!-- presentation -->
  <article class="piece slide title" style="left:1002px;top:14px;width:92px;height:68px">
    <div class="brand on-light"><span class="dot"></span>Summit Vigor &amp; Wellness</div>
    <div class="welcome">Welcome to Our</div><div class="name">Presentation Name</div><div class="desc">Description</div>
    <div class="bar"></div>
  </article>
  <article class="piece slide" style="left:1100px;top:14px;width:92px;height:68px">
    <span class="corner"></span><h3>Heading Here</h3><h4>Sub Heading</h4>
    <div class="photos"><div>Photo</div><div>Photo</div><div>Photo</div><div>Photo</div></div>
    <p>Team member name and title with a short note on their coaching focus.</p>
    <div class="bar"></div>
  </article>
  <article class="piece slide" style="left:1002px;top:90px;width:92px;height:68px">
    <span class="corner"></span><h3>Heading Here</h3><h4>Sub Heading</h4>
    <p><b style="color:var(--green)">Group 1</b> Strength sessions twice a week with a simple warm up and cool down.</p>
    <p><b style="color:var(--green)">Group 2</b> Mobility work and light cardio on rest days.</p>
    <p><b style="color:var(--green)">Group 3</b> Monthly check in on goals and nutrition.</p>
    <div class="bar"></div>
  </article>
  <article class="piece slide" style="left:1100px;top:90px;width:92px;height:68px">
    <span class="corner"></span><h3>Heading Here</h3><h4>Sub Heading</h4>
    <svg width="40" height="28" viewBox="0 0 40 28" style="margin-top:3px"><line x1="2" y1="27" x2="38" y2="27" stroke="#bbb" stroke-width=".4"/><rect x="4" y="4" width="5" height="23" fill="#8dc63f"/><rect x="11" y="10" width="5" height="17" fill="#a9d651"/><rect x="18" y="7" width="5" height="20" fill="#8dc63f"/><rect x="25" y="14" width="5" height="13" fill="#a9d651"/><rect x="32" y="18" width="5" height="9" fill="#8dc63f"/></svg>
    <p style="position:absolute;left:50px;top:16px;width:38px">Progress across five months of training shows steady gains.</p>
    <div class="bar"></div>
  </article>
  <article class="piece slide" style="left:1002px;top:166px;width:92px;height:68px">
    <span class="corner"></span><h3>Heading Here</h3><h4>Sub Heading</h4>
    <p style="width:46px">Most clients reach their first goal within twelve weeks of regular training and coaching.</p>
    <svg width="24" height="24" viewBox="0 0 24 24" style="position:absolute;left:62px;top:22px"><circle cx="12" cy="12" r="10" fill="#c4e05a"/><path d="M12 12 L12 2 A10 10 0 0 1 21 16 Z" fill="#5f9a2a"/><path d="M12 12 L21 16 A10 10 0 0 1 8 21 Z" fill="#8dc63f"/></svg>
    <div class="bar"></div>
  </article>
  <article class="piece slide closing" style="left:1100px;top:166px;width:92px;height:68px">
    <div class="big">Thanks</div><div class="small">For Coming</div>
  </article>

  <!-- lower row: pocket folder interior, discs, magnets, screens -->
  <div class="piece" style="left:476px;top:140px;width:120px;height:70px;background:var(--paper)">
    <div role="img" aria-label="Green gradient pocket panels" style="position:absolute;left:6px;right:6px;bottom:4px;height:26px;background:linear-gradient(90deg,var(--green),var(--green-light))"></div>
  </div>
  <div class="magnet" style="left:484px;top:222px;background:var(--paper)"><div class="brand on-light"><span class="dot"></span>SVW</div></div>
  <div class="magnet" style="left:510px;top:222px;background:var(--green)"><div class="brand on-green"><span class="dot"></span>SVW</div></div>
  <div class="magnet" style="left:536px;top:222px;background:var(--grey)"><div class="brand on-dark"><span class="dot"></span>SVW</div></div>
  <div class="magnet" style="left:562px;top:222px;background:var(--paper)"><div class="brand on-light"><span class="dot"></span>SVW</div></div>

  <div class="disc green" style="left:680px;top:128px;width:58px;height:58px"><div class="brand on-green"><span class="dot"></span>Summit Vigor</div><div class="hole"></div></div>
  <div class="disc grey" style="left:746px;top:128px;width:58px;height:58px"><div class="brand on-dark"><span class="dot"></span>Summit Vigor</div><div class="hole"></div></div>
  <div class="disc white" style="left:680px;top:192px;width:58px;height:58px"><div class="brand on-light"><span class="dot"></span>Summit Vigor</div><div class="hole"></div></div>
  <div class="disc green" style="left:746px;top:192px;width:58px;height:58px"><div class="brand on-green"><span class="dot"></span>Summit Vigor</div><div class="hole"></div></div>

  <div class="piece screen green" style="left:818px;top:144px;width:58px;height:38px"><div class="brand on-green"><span class="dot"></span>Summit Vigor</div></div>
  <div class="piece screen light" style="left:818px;top:196px;width:58px;height:38px"><div class="brand on-light"><span class="dot"></span>Summit Vigor</div></div>
  <div class="piece screen light" style="left:890px;top:144px;width:56px;height:40px"><div class="brand on-light"><span class="dot"></span>Summit Vigor</div></div>
  <div class="piece screen black" style="left:890px;top:196px;width:56px;height:40px"><div class="brand on-dark"><span class="dot"></span>Summit Vigor</div></div>
  <div class="piece screen light" style="left:962px;top:146px;width:16px;height:34px"></div>
  <div class="piece screen black" style="left:962px;top:198px;width:16px;height:34px"></div>

</main>
</body>
</html>
```